QuillMark Business Cards

I need a business card designed for QuillMark. To get an idea of what we do please visit https://formvault.example/para-creadores-3

```html
<!DOCTYPE html>
<html lang="en">
<head>
<meta charset="utf-8">
<title>QuillMark Business Cards</title>
<link rel="stylesheet" href="https://fonts.googleapis.com/css2?family=Montserrat:wght@400;500&family=Arimo:wght@700&family=Lato:wght@300&display=swap">
<style>
  :root {
    --backdrop: #1f3338;
    --slate: #3d4c53;
    --slate-light: #48575e;
    --amber: #dea055;
    --amber-deep: #d08b3c;
    --paper: #ececec;
    --ink: #2e3d44;
    --ink-soft: #4a555a;
    --white: #f4f4f4;
  }
  * { margin: 0; padding: 0; box-sizing: border-box; }
  html, body { width: 1200px; height: 905px; overflow: hidden; }
  body { background: var(--backdrop); position: relative; }

  .card {
    position: absolute;
    width: 564px;
    height: 324px;
    overflow: hidden;
    box-shadow: 0 14px 28px rgba(0,0,0,0.35);
  }

  /* Front */
  .card-front {
    left: 417px; top: 78px;
    background: linear-gradient(200deg, var(--slate-light) 0%, var(--slate) 60%, #36454b 100%);
  }
  .front-band {
    position: absolute;
    left: 109px; top: 0;
    width: 69px; height: 100%;
    background: var(--amber);
  }
  .brand-mark {
    position: absolute;
    left: 126px; top: 144px;
    width: 35px; height: 35px;
    background: var(--slate);
  }
  .brand-name {
    position: absolute;
    left: 205px; top: 139px;
    font-family: "Montserrat", sans-serif;
    font-weight: 400;
    font-size: 31px;
    letter-spacing: 0.3em;
    color: var(--white);
    line-height: 1;
  }
  .brand-tagline {
    position: absolute;
    left: 206px; top: 174px;
    display: flex;
    align-items: center;
    font-family: "Montserrat", sans-serif;
    font-weight: 500;
    font-size: 9px;
    letter-spacing: 0.48em;
    color: var(--amber);
  }
  .brand-tagline .rule {
    display: block;
    width: 100px;
    height: 1px;
    background: var(--white);
    margin-left: 2px;
  }

  /* Back */
  .card-back {
    left: 416px; top: 464px;
    background: linear-gradient(200deg, #f1f1f1 0%, var(--paper) 50%, #d9d9d9 100%);
  }
  .holder {
    position: absolute;
    right: 52px; top: 94px;
    text-align: right;
    font-family: "Arimo", sans-serif;
    font-weight: 700;
    color: var(--ink);
    line-height: 1;
  }
  .holder-name { font-size: 20px; letter-spacing: 0.01em; }
  .holder-role { font-size: 15px; margin-top: 6px; }

  .contact-list {
    position: absolute;
    right: 45px; top: 146px;
    list-style: none;
    font-family: "Lato", sans-serif;
    font-weight: 300;
    font-size: 12.5px;
    color: var(--ink-soft);
  }
  .contact-item {
    display: flex;
    align-items: center;
    justify-content: flex-end;
    gap: 10px;
    text-align: right;
    line-height: 1.25;
  }
  .contact-item + .contact-item { margin-top: 4px; }
  .contact-item.single { height: 28px; }
  .contact-item.double { height: 34px; }
  .contact-icon { width: 27px; height: 27px; flex: none; }
</style>
</head>
<body>

<section class="card card-front" aria-label="Card front">
  <div class="front-band"></div>
  <div class="brand-mark"></div>
  <div class="brand-name">QUILLMARK</div>
  <div class="brand-tagline">DIGITAL NOTARY<span class="rule"></span></div>
</section>

<section class="card card-back" aria-label="Card back">
  <div class="holder">
    <div class="holder-name">DANA WHITFIELD</div>
    <div class="holder-role">HR MANAGER</div>
  </div>

  <ul class="contact-list">
    <li class="contact-item single">
      <span>(555) 014-2290</span>
      <svg class="contact-icon" viewBox="0 0 28 28" aria-hidden="true">
        <circle cx="14" cy="14" r="14" fill="var(--amber-deep)"/>
        <path d="M10 8.5l2.5 2.8-1.4 1.6c.9 1.8 2.2 3.1 4 4l1.6-1.4 2.8 2.5-1.6 2c-4.8-.4-9.3-4.9-9.7-9.7z" fill="#fff"/>
      </svg>
    </li>
    <li class="contact-item double">
      <span>48 Harbor Lane, Suite 12,<br>Fairview, CA 90000</span>
      <svg class="contact-icon" viewBox="0 0 28 28" aria-hidden="true">
        <circle cx="14" cy="14" r="14" fill="var(--amber-deep)"/>
        <path d="M14 6.5a5.2 5.2 0 0 0-5.2 5.2c0 3.9 5.2 9.8 5.2 9.8s5.2-5.9 5.2-9.8A5.2 5.2 0 0 0 14 6.5z" fill="#fff"/>
        <circle cx="14" cy="11.7" r="2" fill="var(--amber-deep)"/>
      </svg>
    </li>
    <li class="contact-item single">
      <span>dana@formvault.example</span>
      <svg class="contact-icon" viewBox="0 0 28 28" aria-hidden="true">
        <circle cx="14" cy="14" r="14" fill="var(--amber-deep)"/>
        <rect x="7.5" y="9.5" width="13" height="9" fill="none" stroke="#fff" stroke-width="1.3"/>
        <path d="M7.5 9.5l6.5 5 6.5-5M7.5 18.5l4.8-4.3M20.5 18.5l-4.8-4.3" fill="none" stroke="#fff" stroke-width="1.2"/>
      </svg>
    </li>
    <li class="contact-item single">
      <span>www.formvault.example</span>
      <svg class="contact-icon" viewBox="0 0 28 28" aria-hidden="true">
        <circle cx="14" cy="14" r="14" fill="var(--amber-deep)"/>
        <g fill="none" stroke="#fff" stroke-width="1.1">
          <circle cx="14" cy="14" r="7"/>
          <ellipse cx="14" cy="14" rx="3" ry="7"/>
          <path d="M7 14h14M8 10.5h12M8 17.5h12M14 7v14"/>
        </g>
      </svg>
    </li>
  </ul>
</section>

</body>
</html>
```